Real Estate Agent who sells beach front condos needs a template for a monthly postcard campaign.

Marcy Tillford, Homebroker with Quenlow Real Estate and Development, Licensed in Florida and Alabama, 251-374-5820, marcytillford.realtor, marcyktillford@mailbox-example.com. Need a postcard template which will allow me to type in recipe instructions and insert a photo of the finished food product. The recipe and photo will change every month, so I need this to be something I can easily change and reorder every month. I sell beach condos primarily. I'd like large photos of the food. Glossy card on both sides.

Target Market(s)

buyers and sellers of homes, condos, lots

Industry/Entity Type

Real Estate Agent

Requirements
Must have
• my contact information, my photo, my company name (Quenlow Real Estate and Development), the Equal Dwelling Logo, the Homebroker Logo, the statement "Contact me for all your Real Estate needs!", a template on the front side that will let me change the photograph at will, and a template on the back side that will let me type words.
Nice to have
• For my contact info and photo to stand out also.

```html
<!DOCTYPE html>
<html lang="en">
<head>
<meta charset="utf-8">
<title>Recipe Postcard – Italian Caserole</title>
<link href="https://fonts.googleapis.com/css2?family=Sacramento&family=Josefin+Sans:wght@300;400&family=Lato:ital,wght@0,300;0,400;1,300&display=swap" rel="stylesheet">
<style>
  :root{
    --page:#e4e2dd;
    --cream:#efece2;
    --white:#ffffff;
    --taupe:#b8ad92;
    --ink:#4a3b2f;
    --ink-soft:#6b5a4a;
    --band-ink:#5a4a3a;
    --accent:#8c6c4c;
    --rule:#d9d3c4;
    --gold:#e2c84a;
    --photo-a:#5e5650;
    --photo-b:#b8372c;
    --photo-c:#4f7a35;
    --photo-d:#d8b868;
  }
  *{box-sizing:border-box;margin:0;padding:0}
  html,body{width:1200px;height:800px;overflow:hidden;background:var(--page)}
  body{position:relative;font-family:"Lato",sans-serif;color:var(--ink)}

  .postcard{position:absolute;left:230px;width:740px;height:370px;background:var(--cream);
    box-shadow:0 4px 14px rgba(0,0,0,.18);overflow:hidden}
  .postcard--back{top:20px}
  .postcard--front{top:410px}

  .food-photo{position:absolute;left:0;top:0;
    background:
      radial-gradient(ellipse at 20% 35%, var(--photo-b) 0%, transparent 40%),
      radial-gradient(ellipse at 55% 20%, var(--photo-c) 0%, transparent 38%),
      radial-gradient(ellipse at 80% 70%, var(--photo-d) 0%, transparent 35%),
      radial-gradient(ellipse at 85% 10%, #c0443b 0%, transparent 30%),
      linear-gradient(135deg, #6e6660, var(--photo-a));}
  .grid-lines{position:absolute;left:0;top:0;pointer-events:none}

  .recipe-tab{position:absolute;width:108px;height:32px;background:var(--cream);
    border-radius:16px 16px 0 0;text-align:center;font-family:"Josefin Sans",sans-serif;
    font-size:14px;letter-spacing:.5px;color:var(--ink-soft);line-height:36px}

  .dish-title{position:absolute;font-family:"Sacramento",cursive;font-weight:400;color:var(--ink);line-height:1;white-space:nowrap}
  .dish-subtitle{position:absolute;font-family:"Josefin Sans",sans-serif;font-weight:300;
    color:var(--accent);letter-spacing:.3px;text-transform:uppercase;white-space:nowrap}

  /* front */
  .postcard--front .food-photo{width:740px;height:270px}
  .postcard--front .recipe-tab{left:304px;top:240px}
  .postcard--front .dish-title{left:170px;top:284px;font-size:60px}
  .postcard--front .dish-subtitle{left:222px;top:342px;font-size:12.5px}

  /* back */
  .postcard--back .food-photo{width:370px;height:270px}
  .postcard--back .recipe-tab{left:138px;top:250px;width:64px;height:20px;font-size:9px;line-height:23px;border-radius:10px 10px 0 0}
  .postcard--back .dish-title{left:82px;top:292px;font-size:36px}
  .postcard--back .dish-subtitle{left:92px;top:330px;font-size:7.2px}

  .recipe-text{position:absolute;left:370px;top:0;width:370px;height:270px;background:var(--white)}
  .ingredients{position:absolute;left:12px;top:14px;width:96px}
  .section-heading{font-family:"Sacramento",cursive;font-weight:400;color:var(--ink-soft);line-height:1}
  .ingredients .section-heading{font-size:20px;margin-bottom:6px}
  .ingredients li{list-style:none;font-style:italic;font-weight:300;font-size:6.2px;line-height:9.4px;color:var(--ink);white-space:nowrap}
  .column-rule{position:absolute;left:114px;top:0;width:1px;height:270px;background:var(--rule)}
  .preparation{position:absolute;left:126px;top:8px;width:230px}
  .preparation .section-heading{font-size:34px;margin-bottom:14px}
  .preparation p{font-size:7px;line-height:10px;font-weight:300;margin-bottom:9px;color:var(--ink)}
  .utensils{position:absolute;right:12px;top:4px}

  .agent-band{position:absolute;left:370px;top:270px;width:370px;height:100px;background:var(--taupe);color:var(--band-ink)}
  .agent-portrait{position:absolute;left:22px;top:-22px;width:86px;height:86px;border-radius:50%;
    border:3px solid var(--white);background:radial-gradient(circle at 50% 40%, #d9c6a0, #8e8a86)}
  .agent-details{position:absolute;left:124px;top:12px;width:236px}
  .agent-name{font-size:12px;font-weight:400}
  .agent-role{font-size:6.8px;line-height:9.5px}
  .agent-tagline{margin-top:5px;font-size:7px;line-height:9.5px;font-style:italic}
  .agent-contact{margin-top:4px;font-size:6.4px;line-height:8.8px}
  .affiliations{position:absolute;right:12px;bottom:9px;display:flex;gap:10px}
  .affiliation{display:flex;align-items:center;gap:3px;font-size:6.4px;line-height:1}
  .affiliation-mark{width:9px;height:9px;background:var(--band-ink)}
  .affiliation-mark--round{border-radius:50%}
</style>
</head>
<body>

<section class="postcard postcard--back" aria-label="Postcard back">
  <div class="food-photo" role="img" aria-label="Italian ingredients on a wooden table: tomatoes, basil, garlic, olives, spaghetti, olive oil and cheese"></div>
  <svg class="grid-lines" width="370" height="270" aria-hidden="true">
    <line x1="128" y1="0" x2="128" y2="270" stroke="#fff" stroke-width="1.2"/>
    <line x1="0" y1="26" x2="370" y2="26" stroke="#fff" stroke-width="1.2"/>
  </svg>
  <div class="recipe-tab">RECIPE 1</div>
  <h2 class="dish-title">Italian caserole</h2>
  <p class="dish-subtitle">A refreshing summer dish for the whole family</p>

  <div class="recipe-text">
    <div class="ingredients">
      <h3 class="section-heading">Ingredients</h3>
      <ul>
        <li>200g couscous</li>
        <li>zest and juice 1 lemon</li>
        <li>2 tbsp olive oil</li>
        <li>2 tbsp tahini paste</li>
        <li>1 garlic clove, crushed</li>
        <li>griddled courgettes</li>
        <li>4 tomatoes, roughly chopped</li>
        <li>200g pack feta cheese, crumbled</li>
        <li>small pack mint, leaves picked</li>
        <li>small pack parsley, leaves picked</li>
        <li>1 red chilli, deseeded and sliced</li>
      </ul>
    </div>
    <div class="column-rule"></div>
    <div class="preparation">
      <h3 class="section-heading">Preparation</h3>
      <p>Put the couscous in a heatproof bowl and pour over boiling water to just cover.</p>
      <p>Cover with cling film and leave to stand for 5 mins.</p>
      <p>Mix the lemon zest and juice, oil, tahini and garlic, and season to taste. Fluff the prepared couscous and season. Spoon onto a large serving platter and scatter over the courgettes, tomatoes, feta, herbs and chilli. Drizzle over the dressing.</p>
    </div>
    <svg class="utensils" width="60" height="62" viewBox="0 0 60 62" fill="none" stroke="var(--gold)" stroke-width="1.2" aria-hidden="true">
      <path d="M8 2v12M12 2v12M16 2v12M8 14q4 6 8 0M12 17v43"/>
      <ellipse cx="30" cy="9" rx="5" ry="8"/><path d="M30 17v43"/>
      <path d="M48 2q-6 10 0 20q6-10 0-20M48 2q-3 10 0 20q3-10 0-20M48 22v38"/>
    </svg>
  </div>

  <div class="agent-band">
    <div class="agent-portrait" role="img" aria-label="Agent portrait photo"></div>
    <div class="agent-details">
      <p class="agent-name">Marcy Tillford</p>
      <p class="agent-role">Homebroker with Quenlow Real Estate and Development.</p>
      <p class="agent-role">Licensed in Florida and Alabama.</p>
      <p class="agent-tagline">Contact me for all your Real Estate needs!</p>
      <p class="agent-contact">T: 251-374-5820<br>W: marcytillford.realtor<br>E: marcyktillford@mailbox-example.com</p>
    </div>
    <div class="affiliations">
      <span class="affiliation"><span class="affiliation-mark"></span>Equal Dwelling</span>
      <span class="affiliation"><span class="affiliation-mark affiliation-mark--round"></span>Homebroker</span>
    </div>
  </div>
</section>

<section class="postcard postcard--front" aria-label="Postcard front">
  <div class="food-photo" role="img" aria-label="Italian ingredients on a wooden table: tomatoes, basil, garlic, olives, spaghetti, olive oil and cheese"></div>
  <svg class="grid-lines" width="740" height="270" aria-hidden="true">
    <line x1="252" y1="0" x2="252" y2="270" stroke="#fff" stroke-width="1.5"/>
    <line x1="0" y1="30" x2="740" y2="30" stroke="#fff" stroke-width="1.5"/>
  </svg>
  <div class="recipe-tab">RECIPE 1</div>
  <h1 class="dish-title">Italian caserole</h1>
  <p class="dish-subtitle">A refreshing summer dish for the whole family</p>
</section>

</body>
</html>
```